Webdesign für Coaching von Erwachsenen und Kindern
Zielgruppe
Ich coache Erwachsene und Kinder mit den Methoden des NLP. Meine Zielgruppe sind primär Eltern und auch Lehrer. Mein Ziel sind mehr glückliche Kinder, indem ich primär die Eltern und teilweise auch die Kinder coache.
Mir ist es wichtig souverän und nicht wie eine Kindergärtnerin zu wirken.
Aufgabenstellung
Meine Website: www.coach-merlinger.ch ist mit Wordpress erstellt.
Das Logo besteht bereits und soll so belassen werden. Die Farben des Logos dürfen aufgegriffen werden. Es soll alles zusammenpassen und 'rund' wirken.
Mir gefällt zum Beispiel die Website lumaquo.ch oder Pflegewerk-nord.ch

```html
<!DOCTYPE html>
<html lang="de">
<head>
<meta charset="utf-8">
<title>Johanna Merlinger – Coaching</title>
<link rel="stylesheet" href="https://fonts.googleapis.com/css2?family=Caveat:wght@400;700&family=Poppins:wght@400;500;600&display=swap">
<style>
:root{
  --navy:#0b3a86;
  --blue:#1a72c4;
  --pale:#dde7f3;
  --hero:#eef1f6;
  --ink:#333a45;
  --white:#ffffff;
  --offwhite:#fdfdfd;
  --star:#f0a868;
  --quote:#d3d7dd;
}
*{box-sizing:border-box;margin:0;padding:0}
html,body{width:1200px;height:4482px;overflow:hidden}
body{position:relative;background:var(--offwhite);font-family:'Poppins',sans-serif;color:var(--ink);font-size:13.5px;line-height:1.6}
.abs{position:absolute}
.script{font-family:'Caveat',cursive;color:var(--navy);font-weight:400;line-height:1.15}
.script b{font-weight:700}
p{margin-bottom:18px}
.btn{position:absolute;display:flex;align-items:center;justify-content:center;background:var(--blue);color:var(--white);border:2px solid var(--navy);border-radius:24px;font-size:12.5px;font-weight:600;letter-spacing:.2px;text-transform:uppercase}

/* hero */
.hero{left:0;top:0;width:1200px;height:638px;background:var(--hero)}
.nav{top:86px;left:110px;display:flex;gap:37px;font-size:13.5px;color:#222}
.nav .active{border-bottom:2px solid var(--navy);padding-bottom:4px}
.brand{top:70px;left:460px;width:280px;display:flex;align-items:center;gap:12px;justify-content:center}
.brand .dot{width:16px;height:16px;border-radius:50%;background:var(--navy)}
.brand span{font-size:22px;font-weight:500;color:var(--navy)}
.mail{top:86px;left:806px;font-size:13.5px;color:#222;display:flex;align-items:center;gap:8px}
.hero h1{top:226px;left:110px;font-size:50px}
.hero .lead{top:420px;left:110px;width:560px}
.hero-photo{left:748px;top:140px;width:312px;height:498px;background:linear-gradient(180deg,#e9ebef,#d8d3cc);border-radius:4px}

/* nlp */
.nlp{left:0;top:638px;width:1200px;height:640px;background:var(--pale)}
.nlp-title{top:718px;left:0;width:1200px;text-align:center;font-size:48px}
.nlp-intro{top:782px;left:330px;width:540px;text-align:center}
.benefit{width:240px;text-align:center}
.benefit .ring{width:73px;height:73px;margin:0 auto 22px;display:block}
.benefit h3{font-size:21px;font-weight:400;color:#111;margin-bottom:12px}
.benefit p{font-size:13px}

/* about */
.about h2{top:1312px;left:110px;font-size:50px}
.about .text{top:1378px;left:110px;width:440px}
.about-photo{left:617px;top:1315px;width:583px;height:520px;background:linear-gradient(160deg,#d2d5d8,#9aa0a8 60%,#2b2f36)}

/* offer */
.offer-photo{left:183px;top:2002px;width:372px;height:372px;border-radius:50%;border:3px solid var(--navy);padding:6px;background:var(--white)}
.offer-photo div{width:100%;height:100%;border-radius:50%;background:linear-gradient(180deg,#eceeef,#c9b8a4)}
.offer h2{top:1992px;left:612px;font-size:50px}
.offer .text{top:2053px;left:612px;width:480px}
.offer .hl{color:var(--navy);font-weight:600}
.offer .more{top:2438px;left:210px;width:780px;text-align:center}

/* testimonials */
.reviews h2{top:3083px;left:110px;font-size:50px}
.arrow{width:52px;height:52px;border-radius:50%;background:var(--blue);border:2px solid var(--navy);display:flex;align-items:center;justify-content:center}
.card{background:var(--white);border-radius:12px;padding:30px;width:308px}
.card .quote{font-family:Georgia,serif;font-size:80px;line-height:.8;color:var(--quote);height:46px}
.card p{margin:14px 0 18px}
.author{display:flex;align-items:center;gap:16px}
.avatar{width:48px;height:48px;border-radius:50%;background:linear-gradient(160deg,#a89278,#4a3a30)}
.author strong{font-size:13px;font-weight:600;color:#222;display:block}
.stars{color:var(--star);font-size:18px;letter-spacing:2px;line-height:1}

/* contact */
.contact h2{top:3900px;left:110px;font-size:48px;line-height:1.0}
.contact .lead{top:4020px;left:110px;width:440px}
.info{left:110px;display:flex;gap:20px;align-items:center}
.info strong{font-weight:600;color:#111;display:block}
.form h3{top:4014px;left:612px;font-size:28px;font-weight:400;color:var(--navy);line-height:1.2}
.field{border:1.5px solid var(--blue);background:var(--white);color:#8a93a6;font-size:13px;padding:12px 14px}

/* footer */
.footer{left:0;top:4400px;width:1200px;height:82px;background:var(--pale);display:flex;justify-content:center;align-items:center;gap:37px;font-size:13px;font-weight:500;color:#111;text-transform:uppercase}
</style>
</head>
<body>

<section class="hero abs">
  <nav class="nav abs"><span>Angebote</span><span class="active">Über Mich</span><span>Kontakt</span></nav>
  <div class="brand abs"><i class="dot"></i><span>Johanna Merlinger</span></div>
  <div class="mail abs">
    <svg width="15" height="12" viewBox="0 0 15 12"><rect x="1" y="1" width="13" height="10" rx="1.5" fill="none" stroke="#0b3a86" stroke-width="1.6"/><path d="M1.5 2 7.5 7 13.5 2" fill="none" stroke="#0b3a86" stroke-width="1.6"/></svg>
    kontakt@coach-merlinger.ch
  </div>
  <h1 class="script abs"><b>Glückliche Kinder</b> durch<br>entspannte Eltern,<br>Lehrerinnen und Lehrer</h1>
  <p class="lead abs">Ich coache Eltern, Lehrerinnen und Lehrer und Kinder im Einzelsetting und biete Workshops für mehrere Personen an.</p>
  <a class="btn" style="left:110px;top:496px;width:198px;height:44px">Zum Kontaktformular</a>
  <div class="hero-photo abs" role="img" aria-label="Foto eines lachenden blonden Mädchens im hellen Strickpullover"></div>
</section>

<section class="nlp abs"></section>
<svg class="abs" style="left:0;top:1120px" width="1200" height="200" viewBox="0 0 1200 200">
  <path d="M0 140 C160 40 330 110 520 120 C760 135 900 20 1200 12 L1200 200 L0 200Z" fill="#fdfdfd"/>
</svg>
<h2 class="script abs nlp-title">Neuro-Linguistisches <b>Proagrammieren</b></h2>
<p class="abs nlp-intro">Wollen Sie Leichtigkeit, eine einfache Kommunikation mit ihrem Kind und weniger Ängste? Mehr Vertrauen und Zuversicht und weniger Streit?</p>
<div class="benefit abs" style="left:163px;top:873px">
  <svg class="ring" viewBox="0 0 73 73"><circle cx="36.5" cy="36.5" r="34" fill="none" stroke="#0b3a86" stroke-width="2"/><circle cx="36.5" cy="36.5" r="27" fill="none" stroke="#1a72c4" stroke-width="1"/><path d="M27 37 34 44 47 30" fill="none" stroke="#0b3a86" stroke-width="2.4" stroke-linecap="round" stroke-linejoin="round"/></svg>
  <h3>Vorteil 2</h3>
  <p>Lorem ipsum dolor sit amet, consectetur adipiscing elit, sed do eiusmod tempor incididunt ut Risus commodo viverra accumsan lacus vel facilisis.</p>
</div>
<div class="benefit abs" style="left:480px;top:873px">
  <svg class="ring" viewBox="0 0 73 73"><circle cx="36.5" cy="36.5" r="34" fill="none" stroke="#0b3a86" stroke-width="2"/><circle cx="36.5" cy="36.5" r="27" fill="none" stroke="#1a72c4" stroke-width="1"/><path d="M27 37 34 44 47 30" fill="none" stroke="#0b3a86" stroke-width="2.4" stroke-linecap="round" stroke-linejoin="round"/></svg>
  <h3>Vorteil 2</h3>
  <p>Lorem ipsum dolor sit amet, consectetur adipiscing elit, sed do eiusmod tempor incididunt ut Risus commodo viverra accumsan lacus vel facilisis.</p>
</div>
<div class="benefit abs" style="left:788px;top:873px">
  <svg class="ring" viewBox="0 0 73 73"><circle cx="36.5" cy="36.5" r="34" fill="none" stroke="#0b3a86" stroke-width="2"/><circle cx="36.5" cy="36.5" r="27" fill="none" stroke="#1a72c4" stroke-width="1"/><path d="M27 37 34 44 47 30" fill="none" stroke="#0b3a86" stroke-width="2.4" stroke-linecap="round" stroke-linejoin="round"/></svg>
  <h3>Vorteil 2</h3>
  <p>Lorem ipsum dolor sit amet, consectetur adipiscing elit, sed do eiusmod tempor incididunt ut Risus commodo viverra accumsan lacus vel facilisis.</p>
</div>

<svg class="abs" style="left:0;top:1700px" width="520" height="560" viewBox="0 0 520 560">
  <path d="M0 60 C120 -10 260 90 200 220 C150 330 300 420 220 500 C150 560 60 520 0 540Z" fill="#dde7f3"/>
</svg>
<section class="about">
  <h2 class="script abs">Über <b>Mich</b></h2>
  <div class="text abs">
    <p>In einer Grossfamilie aufgewachsen, habe ich schnell gelernt zu helfen und mich um meine kleineren Geschwister zu kümmern.</p>
    <p>Von zu Hause ausgezogen, widmete ich mich erstmals dem Studium der Tiermedizin und arbeitete als Tierärztin.</p>
    <p>Als ich später selbst Mama wurde, habe ich die Begeisterung für das Wohlergehen von Kindern wieder entdeckt und eine Ausbildung zum NLP-Coach gemacht. Diese hilft mir immer wieder auch im Umgang mit meinem eigenen Kind, in der Partnerschaft und in der Kommunikation mit allen anderen Menschen.</p>
    <p>Ich spüre, was mein Gegenüber braucht und was ihm helfen könnte, mache liebevolle Angebote unter Anwendung der Techniken des NLP.</p>
    <p>NLP begeistert mich immer wieder aufs Neue und ich freue mich über jedes Coaching und über jeden Menschen, dem ich weiterhelfen konnte.</p>
  </div>
  <div class="about-photo abs" role="img" aria-label="Porträtfoto der Coachin mit dunklen Haaren, hellblauer Bluse und dunklem Blazer"></div>
</section>

<section class="offer">
  <div class="offer-photo abs" role="img" aria-label="Rundes Foto eines lächelnden Mädchens mit langen Haaren im gestreiften Shirt"><div></div></div>
  <h2 class="script abs">Mein <b>Angebot</b> für Sie</h2>
  <div class="text abs">
    <p>Mila (10) sitzt traurig im Sessel meiner Praxis und erzählt mir, dass sie Angst hat einzuschlafen. Sie sieht dunkle Gestalten mit riesengrossen Händen, die sie von unten packen wollen und ihr Vater muss jeden Abend bei ihr sitzen, bis sie eingeschlafen ist. Kurze Zeit später strahlt die Kleine und erzählt mir begeistert von Katzenbabys, Glitzer und bunten Spielsachen, die sie jetzt anstelle der dunklen Gestalten und Hände sieht.</p>
    <p>Zwei Wochen später sehe ich sie per Zufall auf dem Schulweg. Sie erzählt mir begeistert, dass sie kein einziges Mal mehr ihren Papa zum Einschlafen brauchte.</p>
    <p class="hl">Solche Erfolge motivieren mich in meiner Coaching Tätigkeit. Schon nach zwei oder drei Sitzungen sind die Probleme einfach, schnell und leicht gelöst.</p>
  </div>
  <div class="more abs">
    <p>Ich coache Kinder und Erwachsene, die Ängste haben, die Probleme in der Schule haben und die ein Verhalten zeigen, welches sie nicht mehr haben wollen. Vom Nägelkauen, über Lernschwierigkeiten, bis zu Streit zu Hause oder Angst alleine in die Schule zu laufen oder ins Klassenlager zu fahren.</p>
    <p>Freuen Sie sich auf Frieden, Harmonie und Leichtigkeit zu Hause und in der Schule und kontaktieren Sie mich unverbindlich für ein Erstgespräch. Verbessern Sie Ihre Kommunikation mit Ihrem Kind.</p>
    <p>Im Einzelsetting wird als Erstes gemeinsam ein Ziel definiert, um Sie optimal zu unterstützen. Dieses wird im Laufe des Coachings immer wieder auf dessen Fortschritt geprüft.</p>
    <p>Eine meiner Stärken ist meine klare Kommunikation auf den Punkt, somit sind die Lösungen oftmals einfacher als anfangs vermutet. Indem ich Fragen stelle, die auch mal unangenehm und doch stets liebevoll und wertschätzend sind, finden wir rasch das für Sie passende Vorgehen.</p>
    <p>Beim Coachen von Kindern involviere ich immer auch die Eltern. Oftmals treffe ich zuerst nur die Eltern und die Kinder werden erst zu einem späteren Zeitpunkt involviert. Ich coache vor Ort oder per Videocall.</p>
  </div>
  <a class="btn" style="left:488px;top:2799px;width:224px;height:42px">Zum Kontaktformular</a>
</section>

<svg class="abs" style="left:0;top:2880px" width="1200" height="940" viewBox="0 0 1200 940">
  <path d="M0 30 C120 -10 240 40 360 60 C520 85 640 10 780 20 C930 30 1000 110 1200 60 L1200 900 C1000 860 700 940 400 910 C250 895 100 930 0 900Z" fill="#dde7f3"/>
</svg>
<section class="reviews">
  <h2 class="script abs">Was meine <b>Kunden</b> sagen</h2>
  <div class="arrow abs" style="left:974px;top:3125px"><svg width="26" height="16" viewBox="0 0 26 16"><path d="M25 8H2M9 1 2 8l7 7" fill="none" stroke="#fff" stroke-width="2.4" stroke-linecap="round" stroke-linejoin="round"/></svg></div>
  <div class="arrow abs" style="left:1036px;top:3125px"><svg width="26" height="16" viewBox="0 0 26 16"><path d="M1 8h23M17 1l7 7-7 7" fill="none" stroke="#fff" stroke-width="2.4" stroke-linecap="round" stroke-linejoin="round"/></svg></div>

  <div class="card abs" style="left:110px;top:3252px">
    <div class="quote">“</div>
    <p>Johanna Merlinger ist ein wirklich sehr empathischer Coach! Sie hört total genau hin, gibt unglaublich passendes liebevolles Feedback und hat bei mir immer den Nagel genau auf den Kopf getroffen! Unglaublich, wieviel sich in schon so kurzer Zeit ändert – und das ganz leicht!</p>
    <div class="author"><div class="avatar" role="img" aria-label="Rundes Kundenfoto"></div><div><strong>LEA, 42</strong><span class="stars">★★★★★</span></div></div>
  </div>
  <div class="card abs" style="left:445px;top:3282px">
    <div class="quote">“</div>
    <p>Johanna Merlinger ist ein wirklich sehr empathischer Coach! Sie hört total genau hin, gibt unglaublich passendes liebevolles Feedback und hat bei mir immer den Nagel genau auf den Kopf getroffen! Unglaublich, wieviel sich in schon so kurzer Zeit ändert – und das ganz leicht!</p>
    <div class="author"><div class="avatar" role="img" aria-label="Rundes Kundenfoto"></div><div><strong>LEA, 42</strong><span class="stars">★★★★★</span></div></div>
  </div>
  <div class="card abs" style="left:777px;top:3217px">
    <div class="quote">“</div>
    <p>Johanna Merlinger ist ein wirklich sehr empathischer Coach! Sie hört total genau hin, gibt unglaublich passendes liebevolles Feedback und hat bei mir immer den Nagel genau auf den Kopf getroffen! Unglaublich, wieviel sich in schon so kurzer Zeit ändert – und das ganz leicht!</p>
    <div class="author"><div class="avatar" role="img" aria-label="Rundes Kundenfoto"></div><div><strong>LEA, 42</strong><span class="stars">★★★★★</span></div></div>
  </div>
</section>

<section class="contact">
  <h2 class="script abs">Nehmen Sie <b>Kontakt</b><br>mit mir auf</h2>
  <p class="lead abs">Gerne können Sie mich per Kontaktformular oder E-Mail für ein unverbindliches Erstgespräch kontaktieren, ich freue mich auf Sie!</p>
  <div class="info abs" style="top:4110px">
    <svg width="54" height="54" viewBox="0 0 54 54"><circle cx="27" cy="27" r="25" fill="none" stroke="#0b3a86" stroke-width="1.6"/><circle cx="27" cy="27" r="20" fill="none" stroke="#1a72c4" stroke-width="1"/><path d="M27 38s-8-8-8-14a8 8 0 0 1 16 0c0 6-8 14-8 14z" fill="none" stroke="#0b3a86" stroke-width="1.8"/><circle cx="27" cy="24" r="3" fill="none" stroke="#0b3a86" stroke-width="1.6"/></svg>
    <div><strong>Adresse</strong>Lindenweg 12, CH-6300 Zug</div>
  </div>
  <div class="info abs" style="top:4184px">
    <svg width="54" height="54" viewBox="0 0 54 54"><circle cx="27" cy="27" r="25" fill="none" stroke="#0b3a86" stroke-width="1.6"/><circle cx="27" cy="27" r="20" fill="none" stroke="#1a72c4" stroke-width="1"/><rect x="16" y="19" width="22" height="16" rx="2" fill="none" stroke="#0b3a86" stroke-width="1.8"/><path d="M17 20l10 8 10-8" fill="none" stroke="#0b3a86" stroke-width="1.8"/></svg>
    <div><strong>E-Mail</strong>kontakt@coach-merlinger.ch</div>
  </div>
  <div class="form">
    <h3 class="abs">Kontktformular</h3>
    <div class="field abs" style="left:612px;top:4061px;width:206px;height:46px">Name</div>
    <div class="field abs" style="left:838px;top:4061px;width:206px;height:46px">E-Mail</div>
    <div class="field abs" style="left:612px;top:4132px;width:432px;height:112px">Mitteilung</div>
    <a class="btn" style="left:913px;top:4272px;width:131px;height:42px">Abschicken</a>
  </div>
</section>

<footer class="footer abs"><span>Impressum</span><span>Datenschutz</span></footer>

</body>
</html>
```